Business Card Design for Kidvale (Hires out childrens play areas)

Looking to have a business card designed for a company we just bought. The company rents out childrens play areas.

I have uploaded a couple of examples of the kind of business card style I like. Here are two more examples:

https://quorvastudio.nz/project/bright-romp-branding/
https://imgvaultcdn.com/design_img/8841052/302917/302917_5518203_8841052_b73e19a2_image.jpg

I think a white card will be best due to all the colours in the logo.

Size we require: 3.75" x 2.25" (horizontally orientated) with a 0.125" bleed

Uploaded is two versions of our logo.

Details for the card:
1. My name: Liam Verster
2. Title: Managing Director
3. Phone no: 021 563 417
4. Email: liam@kidvale.co.nz
5. URL: www.kidvale.co.nz
6. Address:
PO Box 318625
Fernlea, Auckland

Let me know if you need anything else.

Target Market(s)

Hospitals, doctors surgeries, bed shops, etc.

Contact Information for Business Card

Details for the card:
1. My name: Liam Verster
3. Phone no: 021 563 417
5. URL: www.kidvale.co.nz
6. Address:
PO Box 318625
Fernlea, Auckland

Requirements
Should not have
• Not too busy.

```html
<!DOCTYPE html>
<html lang="en">
<head>
<meta charset="utf-8">
<title>Kidvale Business Card</title>
<link rel="stylesheet" href="https://fonts.googleapis.com/css2?family=Didact+Gothic&family=Arimo:wght@400&display=swap">
<style>
  :root {
    --page: #e4e4e4;
    --card-white: #ffffff;
    --card-fade: #eeeeee;
    --brand-green: #3cb54a;
    --brand-green-dark: #12994a;
    --brand-purple: #8e2a92;
    --brand-purple-faint: #eadbea;
    --brand-blue: #1565b8;
    --ink: #4a4a4a;
    --ink-light: #5c5c5c;
    --white: #ffffff;
  }
  * { box-sizing: border-box; margin: 0; padding: 0; }
  html, body { width: 1200px; height: 960px; overflow: hidden; }
  body {
    background: var(--page);
    position: relative;
    font-family: "Arimo", Arial, sans-serif;
  }
  .card {
    position: absolute;
    left: 300px;
    width: 600px;
    height: 360px;
    overflow: hidden;
    box-shadow: 0 4px 14px rgba(0,0,0,0.18);
  }
  .card--front {
    top: 80px;
    background: linear-gradient(180deg, var(--card-white) 55%, var(--card-fade) 100%);
  }
  .card--back {
    top: 500px;
    background: var(--brand-green);
    border: 10px solid var(--brand-green-dark);
  }
  .faint-mark {
    position: absolute;
    left: -60px;
    top: 110px;
    width: 340px;
    height: 340px;
    border-radius: 50%;
    background: var(--brand-purple-faint);
    opacity: 0.55;
  }
  .corner-mark {
    position: absolute;
    right: -40px;
    top: -30px;
    width: 110px;
    height: 110px;
    border-radius: 50%;
    background: var(--brand-purple);
  }
  .brand {
    position: absolute;
    display: flex;
    align-items: center;
    gap: 12px;
    font-family: "Didact Gothic", sans-serif;
    font-weight: 400;
    line-height: 1;
  }
  .brand__dot {
    border-radius: 50%;
    flex: none;
  }
  .card--front .brand {
    left: 56px;
    top: 78px;
    font-size: 48px;
    color: var(--brand-blue);
  }
  .card--front .brand__dot {
    width: 34px;
    height: 34px;
    background: var(--brand-blue);
  }
  .contact {
    position: absolute;
    left: 350px;
    top: 112px;
    color: var(--ink);
  }
  .contact__name {
    font-family: "Didact Gothic", sans-serif;
    font-size: 38px;
    font-weight: 400;
    color: var(--brand-green);
    line-height: 1;
    letter-spacing: -0.5px;
  }
  .contact__title {
    font-size: 16px;
    color: var(--ink-light);
    margin-top: 6px;
  }
  .contact__address,
  .contact__lines {
    font-size: 16px;
    line-height: 21px;
    font-style: normal;
    padding-left: 3px;
  }
  .contact__address { margin-top: 24px; }
  .contact__lines { margin-top: 8px; }
  .card--back .brand {
    left: 0;
    right: 0;
    top: 110px;
    justify-content: center;
    font-size: 76px;
    color: var(--white);
  }
  .card--back .brand__dot {
    width: 52px;
    height: 52px;
    background: var(--white);
  }
  .back-url {
    position: absolute;
    left: 0;
    right: 0;
    top: 262px;
    text-align: center;
    font-size: 21px;
    color: var(--white);
  }
</style>
</head>
<body>
  <section class="card card--front">
    <div class="faint-mark" aria-hidden="true"></div>
    <div class="corner-mark" aria-hidden="true"></div>
    <div class="brand"><span class="brand__dot"></span>Kidvale</div>
    <div class="contact">
      <h1 class="contact__name">Liam Verster</h1>
      <p class="contact__title">Managing Director</p>
      <address class="contact__address">PO Box 318625<br>Fernlea, Auckland</address>
      <p class="contact__lines">021 563 417<br>liam@kidvale.co.nz<br>www.kidvale.co.nz</p>
    </div>
  </section>

  <section class="card card--back">
    <div class="brand"><span class="brand__dot"></span>Kidvale</div>
    <p class="back-url">www.kidvale.co.nz</p>
  </section>
</body>
</html>
```